Business Intelligence Application - Reporting Menu and Report Criteria Design

Looking for a fresh, effective and user friendly view for the menu structure and reporting criteria screen format for a business reporting application. Initial format completed, content structure is in place, but we need the 'wow' design.. as its a serious professional report/BI tool it has to fall within certain guidelines for clarity and graphics..but we want it to be slick, friendly, great user experience. There is a large amount of complex content to fit into a small space and we need it to be very inviting, modern and intuitive.. If interested, please review the attachment. We have live screens in operation, but feel these could be improved and looking forward to seeing what great creative suggestions could be made. Please review work done to date in the attached.. We are not looking for a total re-design of everything, all the basic business content/structure is there.. but tell us what we could do to improve this in terms of graphic design... particularly the criteria screens.. thanks!
Updates

Reason: Need a few more days to review designs - thanks for all submissions so far, we will make a selection shortly.

Target Market(s)

Business analysts, hotel operations teams, finance analysts hospitality industry

Industry/Entity Type

Hospitality

Coding

Coded - Design and coding required

Number of Pages Required

4 page

Font styles to use
Sans Serif
Other font styles liked:
• Candara, please see example in deck

Colors
3276b5
3176b5
0255a3
85acd3
33a6d7
cee9f5
85cae6

Requirements
Must have
• sharp clear, logical menu structure, (currently it has 'clicks to sub-menus, we need hover over, slide to sub-menus..) colour, styling.. and most focus on revision of criteria.. right now is somewhat heavy, cumbersome.. keep colour and friendly intuitive process steps.. its heavy analytical stuff.. best of luck!
Should not have
• No grey fonts on white or grey screens! many business apps are not readable or sharp.. or fonts are too small.. colourless, so please avoid that.. see our deck - sharp dark (navy) or black fonts on white, or light shading..

```html
<!DOCTYPE html>
<html lang="en">
<head>
<meta charset="utf-8">
<title>Room Performance – Rollup Criteria</title>
<link rel="stylesheet" href="https://fonts.googleapis.com/css2?family=Open+Sans:wght@300;400;600&display=swap">
<style>
:root{
  --navy:#071a33;
  --navy-band:#1c2c45;
  --navy-line:#13263f;
  --side-text:#c9d3df;
  --accent:#33a6d7;
  --accent-text:#2ab3d9;
  --ink:#1d2733;
  --label:#5d6b78;
  --muted:#9aa6b2;
  --line:#e3e8ed;
  --field-line:#e1e6eb;
  --canvas:#e4eaef;
  --white:#ffffff;
  --tab-dark:#14243c;
}
*{box-sizing:border-box;margin:0;padding:0}
html,body{width:1200px;height:1040px;overflow:hidden}
body{font-family:"Open Sans",Arial,sans-serif;background:var(--canvas);color:var(--ink);position:relative}

/* Top bar */
.topbar{position:absolute;left:0;top:0;width:1200px;height:82px;background:var(--white);box-shadow:0 1px 4px rgba(0,0,0,.08);z-index:2}
.brand{position:absolute;left:24px;top:23px;display:flex;align-items:center;gap:14px}
.brand-mark{width:36px;height:36px;border-radius:50%;background:var(--accent)}
.brand-name{font-size:22px;font-weight:400;color:var(--ink)}
.top-cell{position:absolute;top:0;height:82px;border-left:1px solid var(--line);display:flex;align-items:center;justify-content:center}
.top-search{left:642px;width:84px}
.top-tip{left:726px;width:84px}
.top-user{left:810px;width:306px;justify-content:flex-start;padding-left:24px}
.top-settings{left:1116px;width:84px}
.avatar{width:48px;height:48px;border-radius:50%;background:linear-gradient(135deg,#c9b7a6,#6f5f55);border:3px solid #e8ecef;flex:none}
.user-text{margin-left:14px}
.user-name{font-size:13px;color:var(--ink);font-weight:600}
.user-date{font-size:11px;color:var(--muted);margin-top:3px}
.user-caret{position:absolute;right:22px;top:37px}

/* Sidebar */
.sidebar{position:absolute;left:0;top:82px;width:235px;height:958px;background:var(--navy);color:var(--side-text)}
.nav-title{height:40px;background:var(--navy-band);font-size:12px;letter-spacing:1px;padding:12px 24px;color:#aab6c4}
.nav-item{height:45px;display:flex;align-items:center;padding:0 26px;font-size:12px;font-weight:600;letter-spacing:1px;border-bottom:1px solid var(--navy-line);position:relative}
.nav-item svg.icon{width:14px;height:14px;margin-right:14px}
.nav-item .caret{position:absolute;right:24px;top:19px}
.nav-item.open{color:var(--white);border-bottom:none}
.subnav{position:relative;padding:20px 0 16px 53px;border-bottom:1px solid var(--navy-line);list-style:none}
.subnav::before{content:"";position:absolute;left:31px;top:0;bottom:16px;width:1px;background:#2e4260}
.subnav li{font-size:12px;line-height:29px;position:relative}
.subnav li::before{content:"";position:absolute;left:-22px;top:14px;width:8px;height:1px;background:#4a6080}
.subnav li.current{color:var(--accent-text)}
.sidebar-foot{position:absolute;left:24px;bottom:22px;font-size:12px;color:var(--white)}
.sidebar-foot small{display:block;font-size:10px;color:#b7c1cd;margin-top:4px}

/* Page head */
.page-head{position:absolute;left:235px;top:82px;width:965px;height:132px;background:#f5f7f9}
.page-title{position:absolute;left:23px;top:28px;font-size:24px;font-weight:300;color:var(--ink)}
.breadcrumb{position:absolute;right:24px;top:47px;font-size:11px;color:#aab3bd}
.breadcrumb b{font-weight:400;color:var(--accent)}
.page-tabs{position:absolute;left:25px;top:80px;display:flex;height:52px}
.page-tab{font-size:14px;color:#5d6873;padding:12px 24px 0;height:52px}
.page-tab.active{color:var(--accent);border-bottom:2px solid var(--accent)}

/* Criteria tabs */
.criteria-tabs{position:absolute;left:260px;top:247px;display:flex;gap:4px}
.criteria-tab{width:132px;height:39px;display:flex;align-items:center;justify-content:center;font-size:12.5px;color:#5d6873;background:linear-gradient(#ffffff,#eef1f4);border-radius:3px 3px 0 0}
.criteria-tab.active{background:var(--tab-dark);color:var(--white);box-shadow:inset 0 -2px 0 #0b1628}

/* Panel */
.panel{position:absolute;left:260px;top:286px;width:915px;height:729px;background:var(--white)}
.section-head{height:40px;background:var(--accent);color:var(--white);font-size:12.5px;letter-spacing:.5px;padding:0 24px;display:flex;align-items:center;justify-content:space-between}
.section-head .toggle{font-size:16px;font-weight:300}
.section-body{display:grid;grid-template-columns:420px 420px;column-gap:26px;row-gap:11px;padding:22px 24px 26px}
.section-body.first{padding-bottom:27px}
.field label{display:block;font-size:12px;line-height:16px;color:var(--label);margin-bottom:7px}
.input{height:30px;border:1px solid var(--field-line);border-radius:2px;position:relative;font-size:11px;color:#a9b2bb;padding:7px 12px}
.input.select::after{content:"";position:absolute;right:14px;top:10px;width:5px;height:5px;border-right:1px solid #a9b2bb;border-bottom:1px solid #a9b2bb;transform:rotate(45deg)}
.pair{display:flex;gap:13px}
.pair .input{flex:1}
.input.date svg{position:absolute;right:12px;top:8px}
</style>
</head>
<body>

<header class="topbar">
  <div class="brand"><span class="brand-mark"></span><span class="brand-name">Harborline Hotels</span></div>
  <div class="top-cell top-search">
    <svg width="16" height="16" viewBox="0 0 16 16" fill="none" stroke="#c4cbd2" stroke-width="1.5"><circle cx="9" cy="7" r="5"/><path d="M5.5 10.5 1.5 14.5"/></svg>
  </div>
  <div class="top-cell top-tip">
    <svg width="14" height="18" viewBox="0 0 14 18" fill="#c4cbd2"><path d="M7 0a6 6 0 0 0-3.5 10.9V13h7v-2.1A6 6 0 0 0 7 0z"/><rect x="4" y="14.5" width="6" height="2" rx="1"/></svg>
  </div>
  <div class="top-cell top-user">
    <div class="avatar" role="img" aria-label="Portrait photo of the signed-in user"></div>
    <div class="user-text"><div class="user-name">Welcome Daniel Reyes</div><div class="user-date">Oct 03, 2017</div></div>
    <svg class="user-caret" width="9" height="6" viewBox="0 0 9 6" fill="none" stroke="#b6bec6" stroke-width="1.2"><path d="M1 1l3.5 3.5L8 1"/></svg>
  </div>
  <div class="top-cell top-settings">
    <svg width="18" height="18" viewBox="0 0 18 18" fill="none" stroke="var(--accent)" stroke-width="2.4"><circle cx="9" cy="9" r="3.2" stroke-width="2"/><path stroke-dasharray="2.6 2.1" d="M9 2.2a6.8 6.8 0 1 1 0 13.6A6.8 6.8 0 0 1 9 2.2z"/></svg>
  </div>
</header>

<nav class="sidebar">
  <div class="nav-title">NAVIGATION</div>
  <div class="nav-item">
    <svg class="icon" viewBox="0 0 14 14" fill="#c9d3df"><circle cx="7" cy="3.5" r="3"/><path d="M2 14c0-5 2-7 5-7s5 2 5 7z"/></svg>ADMIN
    <svg class="caret" width="8" height="5" viewBox="0 0 8 5" fill="none" stroke="#8b99aa" stroke-width="1.2"><path d="M1 1l3 3 3-3"/></svg>
  </div>
  <div class="nav-item open">
    <svg class="icon" viewBox="0 0 14 14" fill="#ffffff"><rect x="4" y="0" width="6" height="4"/><rect x="6.3" y="4" width="1.4" height="3"/><rect x="1" y="6.5" width="12" height="1.4"/><rect x="0" y="9" width="4" height="5"/><rect x="5" y="9" width="4" height="5"/><rect x="10" y="9" width="4" height="5"/></svg>MANAGEMENT
    <svg class="caret" width="8" height="5" viewBox="0 0 8 5" fill="none" stroke="#8b99aa" stroke-width="1.2"><path d="M1 1l3 3 3-3"/></svg>
  </div>
  <ul class="subnav">
    <li>Summaries</li>
    <li class="current">Consolidations</li>
    <li>Communication</li>
    <li>Cheat Sheet</li>
    <li>Programs</li>
  </ul>
  <div class="nav-item">
    <svg class="icon" viewBox="0 0 14 14" fill="none" stroke="#c9d3df" stroke-width="2.6"><circle cx="7" cy="7" r="2" stroke-width="1.6"/><path stroke-dasharray="2.2 1.8" d="M7 1.5a5.5 5.5 0 1 1 0 11a5.5 5.5 0 0 1 0-11z"/></svg>INTEL
    <svg class="caret" width="8" height="5" viewBox="0 0 8 5" fill="none" stroke="#8b99aa" stroke-width="1.2"><path d="M1 1l3 3 3-3"/></svg>
  </div>
  <div class="nav-item">
    <svg class="icon" viewBox="0 0 14 14" fill="#c9d3df"><rect x="0" y="0" width="14" height="1.5"/><rect x="1" y="2" width="12" height="7"/><path d="M6.3 9h1.4v2L10 14H8.4L7 12.3 5.6 14H4l2.3-3z"/></svg>PLANNING
    <svg class="caret" width="8" height="5" viewBox="0 0 8 5" fill="none" stroke="#8b99aa" stroke-width="1.2"><path d="M1 1l3 3 3-3"/></svg>
  </div>
  <div class="sidebar-foot">© 2017 Yieldway.<small>All right reserved.</small></div>
</nav>

<section class="page-head">
  <h1 class="page-title">Room Perfomance</h1>
  <div class="breadcrumb">Management &nbsp;/&nbsp; Consolidations &nbsp;/&nbsp; <b>Rooms Perfomance</b></div>
  <div class="page-tabs">
    <div class="page-tab active">Revenue Summary</div>
    <div class="page-tab">Demand &amp; Risk</div>
    <div class="page-tab">Inventory Analysis</div>
    <div class="page-tab">Place Holder</div>
  </div>
</section>

<div class="criteria-tabs">
  <div class="criteria-tab active">Rollup Criteria</div>
  <div class="criteria-tab">Report Criteria</div>
  <div class="criteria-tab">Edit View</div>
  <div class="criteria-tab">Saved View</div>
  <div class="criteria-tab">Export</div>
</div>

<main class="panel">
  <div class="section-head">GEOGRAPHIC / MANAGEMENT REGIONS<span class="toggle">×</span></div>
  <div class="section-body first">
    <div class="field"><label>Division</label><div class="input select"></div></div>
    <div class="field"><label>My Group</label><div class="input select"></div></div>
    <div class="field"><label>Region</label><div class="input select"></div></div>
    <div class="field"><label>Property Search</label><div class="input select"></div></div>
    <div class="field"><label>Area</label><div class="input select"></div></div>
    <div class="field"><label>Property ID</label><div class="input select"></div></div>
    <div class="field"><label>City</label><div class="input select"></div></div>
    <div class="field"><label>Country Search</label><div class="input select"></div></div>
  </div>

  <div class="section-head">OPERATIONAL / BI FILTERS<span class="toggle">×</span></div>
  <div class="section-body">
    <div class="field"><label>Brands</label><div class="input select"></div></div>
    <div class="field"><label>Opening Date</label>
      <div class="pair">
        <div class="input date"><svg width="11" height="11" viewBox="0 0 11 11" fill="none" stroke="#b3bcc5"><rect x=".5" y="1.5" width="10" height="9"/><path d="M.5 4h10"/></svg></div>
        <div class="input date"><svg width="11" height="11" viewBox="0 0 11 11" fill="none" stroke="#b3bcc5"><rect x=".5" y="1.5" width="10" height="9"/><path d="M.5 4h10"/></svg></div>
      </div>
    </div>
    <div class="field"><label>Rating</label><div class="input select"></div></div>
    <div class="field"><label>Room Capacity</label>
      <div class="pair"><div class="input">From: 00</div><div class="input">To: 5000</div></div>
    </div>
    <div class="field"><label>Hotel Type</label><div class="input select"></div></div>
    <div class="field"><label>PMS System</label><div class="input select"></div></div>
    <div class="field"><label>F&amp;B Service</label><div class="input select"></div></div>
    <div class="field"><label>Finance System</label><div class="input select"></div></div>
  </div>

  <div class="section-head">CURRENCY CONVERSION<span class="toggle">+</span></div>
</main>

</body>
</html>
```